Tolvik cards

I want a simple business card that pops.
Logo on one side.
On side two i want.
"Are you thinking about a new building on your property, or renovating an existing structure? Contact".....
Owners Name: Gary Pellman
Owners Phone number: 555-209-4176
Address:4716 Copper Fern RD, Marrow Creek, PA 16099
Committed to Quality, Service, and Integrity

```html
<!DOCTYPE html>
<html lang="en">
<head>
<meta charset="utf-8">
<title>Tolvik Builders LLC – Business Card</title>
<link rel="stylesheet" href="https://fonts.googleapis.com/css2?family=Archivo:wght@400;600;700;800&display=swap">
<style>
  :root {
    --page-bg: #2b2a2a;
    --card-bg: #f1f0ee;
    --brown: #4a3426;
    --tan: #a08a70;
    --text-dark: #2e2622;
    --rule: #c9bba8;
  }
  * { margin: 0; padding: 0; box-sizing: border-box; }
  html, body {
    width: 1200px; height: 576px; overflow: hidden;
    background: var(--page-bg);
    font-family: "Archivo", Arial, sans-serif;
  }
  .canvas { position: relative; width: 1200px; height: 576px; }
  .card {
    position: absolute;
    background: var(--card-bg);
    border-radius: 10px;
    overflow: hidden;
  }
  .card--front { left: 102px; top: 139px; width: 484px; height: 292px; }
  .card--back  { left: 596px; top: 139px; width: 480px; height: 290px; }

  /* front */
  .wordmark {
    position: absolute; left: 46px; top: 114px;
    color: var(--brown); font-weight: 800; line-height: 1;
  }
  .wordmark__name { display: block; font-size: 48px; letter-spacing: -0.5px; }
  .wordmark__sub { display: block; font-size: 14px; letter-spacing: 6.4px; margin-top: 4px; padding-left: 2px; }
  .front-block {
    position: absolute; right: 0; bottom: 0;
    width: 150px; height: 150px; background: var(--brown);
  }

  /* back */
  .back-brand {
    position: absolute; top: 26px; left: 0; width: 100%;
    display: flex; justify-content: center; align-items: center; gap: 18px;
    color: var(--brown); font-weight: 800;
  }
  .back-brand__mark { width: 54px; height: 54px; background: var(--brown); }
  .back-brand__text { line-height: 1; }
  .back-brand__name { display: block; font-size: 38px; letter-spacing: -0.5px; }
  .back-brand__sub { display: block; font-size: 12px; letter-spacing: 4.4px; margin-top: 2px; padding-left: 1px; }

  .pitch-band {
    position: absolute; left: 0; top: 101px; width: 100%; height: 53px;
    background: var(--brown); color: #fff;
    font-weight: 700; font-size: 13px; line-height: 17px; letter-spacing: 0.3px;
    text-align: center; padding-top: 8px; text-transform: uppercase;
  }
  .contact-pill {
    position: absolute; left: 192px; top: 146px; width: 97px; height: 17px;
    border-radius: 9px; background: var(--tan); color: #fff;
    font-weight: 600; font-size: 12px; line-height: 17px; text-align: center; letter-spacing: 0.4px;
  }
  .owner {
    position: absolute; top: 169px; width: 100%; text-align: center;
    font-weight: 700; font-size: 21px; line-height: 26px; letter-spacing: 0.3px; color: var(--brown);
  }
  .owner__last { color: var(--tan); }
  .phone {
    position: absolute; top: 197px; width: 100%; text-align: center;
    font-weight: 700; font-size: 14px; line-height: 18px; color: var(--text-dark);
  }
  .address {
    position: absolute; top: 216px; width: 100%; text-align: center;
    font-size: 12.5px; line-height: 16px; color: var(--tan);
  }
  .rule {
    position: absolute; left: 42px; top: 243px; width: 398px; height: 1px;
    background: var(--rule);
  }
  .tagline {
    position: absolute; top: 254px; width: 100%; text-align: center;
    font-size: 13px; line-height: 17px; color: var(--text-dark);
  }
</style>
</head>
<body>
<main class="canvas">
  <section class="card card--front" aria-label="Card front">
    <div class="wordmark">
      <span class="wordmark__name">TOLVIK</span>
      <span class="wordmark__sub">BUILDERS LLC</span>
    </div>
    <div class="front-block"></div>
  </section>

  <section class="card card--back" aria-label="Card back">
    <div class="back-brand">
      <div class="back-brand__mark"></div>
      <div class="back-brand__text">
        <span class="back-brand__name">TOLVIK</span>
        <span class="back-brand__sub">BUILDERS LLC</span>
      </div>
    </div>
    <p class="pitch-band">Are you thinking about a new building on your<br>property, or renovating an existing structure?</p>
    <div class="contact-pill">CONTACT</div>
    <p class="owner">GARY <span class="owner__last">PELLMAN</span></p>
    <p class="phone">Call: 555-209-4176</p>
    <p class="address">Add.: 4716 Copper Fern RD, Marrow Creek, PA 16099</p>
    <div class="rule"></div>
    <p class="tagline">Committed to Quality, Service &amp; Integrity</p>
  </section>
</main>
</body>
</html>
```